Business Card Design Project

Based on the attached logo we would like have a designed of a business card.
As we are a management, consulting company focused on business development dealing with C-level and one level below we new business cards.
We have decided to use KLR (Keystone Ledger Relations) as the business name in. The legal name will be Keystone Ledger Relations ApS but we will brand us under KLR. The tack line is “Delivering Steady Growth” if we need one.
We want to signal the following:
- Serious
- Professional
- Creating Result
- Capable of thinking out of the box and creative
- Fast reactions we will be there when needed
What we do not want to be view as is:
- To smart
- We know better
- We can fix it yesterday
Our Value Proposition is two sited:
- Increasing revenue
- Reduced sales cost or increased efficiency
Therefore, companies can call us when they want to grow or they need to be more efficient.
Our business cards should have a two sided print with the logo incl. the tack line on one side and the detailed information on the other site.
We need to have the following information on the business cards:
- Name
- Title
- Address incl. country name (Denmark)
- Main number
- Mobile number
- E-mail address
- Wed address
Symbols are welcome to be used to guide for the above information.
Updates

Some of you has requested our specific details so here they come:

- Address incl. country name (Denmark): Hvedelunden 42, 3520 Farum, Denmark

- Main number: +45 7031 5820

- Wed address: www.klrpeaks.example

Mobile no. are +45 xxxx xxxx or +45 2287 4513

Our e-mail looks like this: firstname.seconname@KLRPEAKS.EXAMPLE or for me: jonas.vardell@klrpeaks.example

We need the design (file) as finish as posible so we just need to add personal details before printing.

Target Market(s)

C-level and one level below.

Industry/Entity Type

Legal

Font styles to use
Serif
Sans Serif

Requirements
Must have
• We would like to se suggestions with the logo (with the tackline) on one site and information on the other site where the logo should be without the tack line.
We would like to recieve recommendations for quality of paper to be used to print the business Cards on.
Nice to have
• If the information side could be used as an e-mail signature for regonition it would be viewed as a plus.

```html
<!DOCTYPE html>
<html lang="en">
<head>
<meta charset="UTF-8">
<title>KLR Business Card</title>
<link href="https://fonts.googleapis.com/css2?family=Arimo:wght@400;700&display=swap" rel="stylesheet">
<style>
  :root {
    --page: #f4f5f7;
    --paper: #ffffff;
    --paper-shade: #eceef1;
    --ink-dark: #101214;
    --ink-dark-2: #1c1f23;
    --brand-blue: #1e6fd0;
    --brand-blue-light: #4a9be8;
    --text-grey: #333840;
    --text-light: #eef1f5;
  }
  * { box-sizing: border-box; margin: 0; padding: 0; }
  html, body { width: 1200px; height: 900px; overflow: hidden; }
  body {
    background: var(--page);
    font-family: "Arimo", Arial, sans-serif;
    display: flex;
    align-items: center;
    justify-content: center;
    gap: 40px;
  }
  .card {
    width: 540px;
    height: 310px;
    border-radius: 22px;
    overflow: hidden;
    position: relative;
    box-shadow: 0 10px 24px rgba(0,0,0,0.14);
  }

  /* Information side */
  .card--info { background: var(--ink-dark); }
  .info-head {
    height: 138px;
    background: linear-gradient(180deg, var(--paper) 0%, var(--paper-shade) 100%);
    position: relative;
  }
  .info-head .brand-name {
    position: absolute;
    left: 40px;
    top: 36px;
    font-size: 66px;
    font-weight: 700;
    color: var(--brand-blue);
    letter-spacing: -1px;
  }
  .person {
    position: absolute;
    right: 34px;
    top: 28px;
    text-align: right;
  }
  .person-name { font-size: 20px; font-weight: 700; color: var(--brand-blue); }
  .person-title { font-size: 15px; color: var(--text-grey); margin-top: 3px; }
  .info-stripe {
    height: 14px;
    background: linear-gradient(90deg, var(--brand-blue) 0%, var(--brand-blue-light) 60%, var(--brand-blue) 100%);
  }
  .info-body {
    height: 158px;
    background: linear-gradient(180deg, var(--ink-dark-2) 0%, var(--ink-dark) 100%);
    padding: 12px 0 0 24px;
  }
  .contact-list { list-style: none; }
  .contact-list li {
    display: flex;
    align-items: flex-start;
    gap: 8px;
    color: var(--text-light);
    font-size: 14.5px;
    line-height: 19px;
  }
  .contact-list svg { width: 14px; height: 14px; margin-top: 2px; flex: none; }
  .contact-list .indent { padding-left: 22px; }

  /* Logo side */
  .card--logo {
    background: radial-gradient(ellipse at 50% 40%, #23272c 0%, var(--ink-dark) 75%);
    display: flex;
    flex-direction: column;
    align-items: center;
    justify-content: center;
  }
  .card--logo .brand-name {
    font-size: 168px;
    font-weight: 700;
    color: var(--brand-blue);
    line-height: 1;
    letter-spacing: -4px;
  }
  .tagline {
    margin-top: 10px;
    font-size: 21px;
    font-weight: 700;
    color: var(--brand-blue);
    letter-spacing: 3.5px;
  }
</style>
</head>
<body>
  <section class="card card--info">
    <div class="info-head">
      <div class="brand-name">KLR</div>
      <div class="person">
        <div class="person-name">Mikkel Arnholt</div>
        <div class="person-title">Manager</div>
      </div>
    </div>
    <div class="info-stripe"></div>
    <div class="info-body">
      <ul class="contact-list">
        <li>
          <svg viewBox="0 0 14 14"><path d="M1 7 L7 1.5 L13 7 H11 V12.5 H8.5 V9 H5.5 V12.5 H3 V7 Z" fill="var(--brand-blue-light)"/></svg>
          Address incl. country
        </li>
        <li class="indent">name (Denmark)</li>
        <li>
          <svg viewBox="0 0 14 14"><path d="M3 1.5 L5.5 1.5 L6.5 4.5 L5 5.8 Q6.5 8.5 8.2 9 L9.5 7.5 L12.5 8.5 L12.5 11 Q12 12.8 10 12.5 Q3 11 1.5 4 Q1.3 2 3 1.5 Z" fill="var(--brand-blue-light)"/></svg>
          4570 315 820
        </li>
        <li>
          <svg viewBox="0 0 14 14"><rect x="3.5" y="1" width="7" height="12" rx="1.2" fill="var(--brand-blue-light)"/><rect x="4.8" y="2.5" width="4.4" height="7" fill="var(--ink-dark)"/></svg>
          2287 451 300
        </li>
        <li>
          <svg viewBox="0 0 14 14"><rect x="1" y="3" width="12" height="8.5" rx="1" fill="var(--brand-blue-light)"/><path d="M1.5 3.5 L7 8 L12.5 3.5" stroke="var(--ink-dark)" stroke-width="1.2" fill="none"/></svg>
          klr@klrpeaks.example
        </li>
        <li>
          <svg viewBox="0 0 14 14"><circle cx="7" cy="7" r="5.8" fill="var(--brand-blue-light)"/><g stroke="var(--ink-dark)" stroke-width="0.9" fill="none"><ellipse cx="7" cy="7" rx="2.5" ry="5.8"/><line x1="1.2" y1="7" x2="12.8" y2="7"/></g></svg>
          www.klrpeaks.example
        </li>
      </ul>
    </div>
  </section>

  <section class="card card--logo">
    <div class="brand-name">KLR</div>
    <div class="tagline">Delivering Steady Growth</div>
  </section>
</body>
</html>
```